Business Card Design for a Personal Trainer

I need a business card design for my job as a personal trainer. It should have a unique, modern and exclusive design. On the front there should be only my logo with my name and my job. 0163/2918374 Tobias Kellinger Lindenfeldweg 14 80412 Munich Germany The most important contact information is the web adress. it can be bigger than the rest, but its not necessary. The card should be 8,5cmx5,5cm big. Font: Roboto. Colors: black, white, gray, 56c1ff.

```html
<!DOCTYPE html>
<html lang="de">
<head>
<meta charset="utf-8">
<title>Tobias Kellinger – Visitenkarte</title>
<link rel="stylesheet" href="https://fonts.googleapis.com/css2?family=Roboto:wght@400;500&display=swap">
<style>
  :root {
    --backdrop: #939393;
    --card-light: #ffffff;
    --card-dark: #232323;
    --ink: #1e1e1e;
    --ink-inverse: #ffffff;
    --photo-tone-light: #b4b4b4;
    --photo-tone-dark: #6e6e6e;
  }
  html, body {
    margin: 0;
    padding: 0;
    overflow: hidden;
  }
  body {
    width: 1200px;
    height: 900px;
    background: var(--backdrop);
    position: relative;
    font-family: "Roboto", Arial, sans-serif;
  }
  .card {
    position: absolute;
    top: 200px;
    width: 309px;
    height: 502px;
  }
  .card--contact {
    left: 254px;
    background: var(--card-light);
    color: var(--ink);
    border-radius: 56px 0 56px 0;
  }
  .card--brand {
    left: 628px;
    background: var(--card-dark);
    color: var(--ink-inverse);
    border-radius: 0 56px 0 56px;
  }
  .portrait {
    position: absolute;
    left: 39px;
    top: 58px;
    width: 230px;
    height: 230px;
    border-radius: 50%;
    background: radial-gradient(circle at 50% 40%, var(--photo-tone-light) 0%, #a5a5a5 55%, var(--photo-tone-dark) 100%);
  }
  .contact-list {
    position: absolute;
    left: 32px;
    top: 355px;
    margin: 0;
    padding: 0;
    list-style: none;
    font-size: 16px;
    line-height: 20px;
  }
  .contact-list li {
    display: flex;
    align-items: center;
    gap: 5px;
  }
  .contact-list svg {
    width: 15px;
    height: 15px;
    fill: var(--ink);
    flex: none;
  }
  .address {
    position: absolute;
    left: 33px;
    top: 426px;
    margin: 0;
    font-style: normal;
    font-size: 16px;
    line-height: 21px;
  }
  .brand-name {
    position: absolute;
    left: 0;
    right: 0;
    top: 275px;
    margin: 0;
    text-align: center;
    font-weight: 400;
    font-size: 26px;
    letter-spacing: 0.5px;
  }
  .brand-role {
    position: absolute;
    left: 27px;
    right: 30px;
    top: 303px;
    display: flex;
    align-items: center;
    gap: 6px;
    font-size: 11px;
    letter-spacing: 3px;
    white-space: nowrap;
  }
  .brand-role::before,
  .brand-role::after {
    content: "";
    flex: 1;
    height: 1px;
    background: var(--ink-inverse);
  }
</style>
</head>
<body>
  <section class="card card--contact">
    <div class="portrait" role="img" aria-label="Porträtfoto des Personal Trainers in Schwarz-Weiß"></div>
    <ul class="contact-list">
      <li>
        <svg viewBox="0 0 16 16" aria-hidden="true"><path d="M1 5c0-2 3-3 7-3s7 1 7 3v1h-4V4.5H5V6H1z M3 7h10l1 7H2z M8 9a2 2 0 1 0 0 4 2 2 0 0 0 0-4z"/></svg>
        0163/2918374
      </li>
      <li>
        <svg viewBox="0 0 16 16" aria-hidden="true"><path d="M1 3h14v10H1z M2.5 4.5 8 9l5.5-4.5v-.2h-11z" fill-rule="evenodd"/></svg>
        t.kellinger@postfeld.de
      </li>
      <li>
        <svg viewBox="0 0 16 16" aria-hidden="true"><circle cx="8" cy="8" r="7"/><path d="M5 4c2 0 2 2 4 2s1 3-1 3-2 2-1 4c-3-1-4-4-3-6z M11 10c1 0 2 1 1 2-1 0-1-1-1-2z" fill="#fff"/></svg>
        www.tobiaskellinger.de
      </li>
    </ul>
    <address class="address">
      Lindenfeldweg 14<br>
      80412 München
    </address>
  </section>

  <section class="card card--brand">
    <h1 class="brand-name">TOBIAS KELLINGER</h1>
    <p class="brand-role" style="margin:0">PERSONAL TRAINER</p>
  </section>
</body>
</html>
```